Falcon Breakerworks - Field Service Brochure

We are looking for a one page marketing brochure that includes our rate sheet. I've attached the working we on on the rate page, several photos and several versions of our logo.

```html
<!DOCTYPE html>
<html lang="en">
<head>
<meta charset="utf-8">
<title>Falcon Breakerworks – Field Service Rates</title>
<link href="https://fonts.googleapis.com/css2?family=Jost:wght@300;400;500;600;700&display=swap" rel="stylesheet">
<style>
  :root{
    --stage:#cfd1d4;
    --paper:#f4f5f7;
    --paper-tint:#e6ecf3;
    --navy:#3f5f86;
    --navy-deep:#2f4c70;
    --photo-a:#4f7299;
    --photo-b:#6e8fb3;
    --blue:#2f6fc0;
    --blue-light:#3a90d4;
    --orange:#ea6a22;
    --orange-light:#f08a24;
    --ink:#4a5f7d;
    --white:#ffffff;
  }
  *{box-sizing:border-box;margin:0;padding:0}
  html,body{width:1172px;height:1200px;overflow:hidden}
  body{background:var(--stage);font-family:"Jost",sans-serif;color:var(--ink)}
  .flyer{position:absolute;left:136px;top:18px;width:900px;height:1164px;background:var(--paper);overflow:hidden;box-shadow:0 10px 30px rgba(0,0,0,.18)}
  .flyer__tint{position:absolute;inset:0;width:100%;height:100%}
  .hero{position:absolute;left:0;top:0;width:900px;height:620px;
    background:linear-gradient(160deg,var(--photo-b) 0%,var(--photo-a) 45%,var(--navy) 100%);
    clip-path:polygon(0 0,100% 0,100% 360px,62% 620px,0 620px)}
  .hero__overlay{position:absolute;inset:0;background:rgba(47,76,112,.45)}
  .brand-tab{position:absolute;left:290px;top:0;width:320px;height:210px;background:var(--white);
    clip-path:polygon(0 0,100% 0,100% 158px,50% 210px,0 158px);
    display:flex;flex-direction:column;align-items:center;padding-top:58px}
  .brand-tab__mark{width:32px;height:32px;border-radius:50%;background:var(--navy);margin-bottom:12px}
  .brand-tab__name{font-weight:600;font-size:20px;letter-spacing:.5px;color:var(--navy);text-transform:uppercase}
  .brand-tab__tagline{font-size:10px;color:var(--navy);margin-top:3px}
  .intro{position:absolute;left:150px;top:232px;width:600px;text-align:center;color:var(--white);font-weight:300;font-size:18px;line-height:1.45}
  .rate-card{position:absolute;width:360px;height:312px}
  .rate-card svg{position:absolute;inset:0;width:100%;height:100%}
  .rate-card__body{position:absolute;inset:0;display:flex;flex-direction:column;align-items:center;color:var(--white);text-align:center}
  .rate-card__title{font-weight:600;font-size:24px;margin-top:16px;line-height:1.2}
  .rate-card__sub{font-size:11.5px;line-height:1.25;width:220px;margin-top:2px}
  .rate-card__price{font-weight:600;font-size:21px;margin-top:14px;line-height:1.2}
  .rate-card__note{font-size:12px;margin-top:1px}
  .rate-card--standard{left:60px;top:545px}
  .rate-card--premium{left:490px;top:420px}
  .info{position:absolute}
  .info__title{font-weight:600;font-size:25px;color:var(--navy-deep);margin-bottom:10px}
  .info ul{list-style:none;font-size:14.5px;line-height:1.4}
  .info li{position:relative;padding-left:18px;margin-bottom:3px}
  .info li::before{content:"";position:absolute;left:2px;top:9px;width:5px;height:5px;border-radius:50%;background:var(--ink)}
  .info--minimum{left:490px;top:762px;width:360px}
  .info--expenses{left:75px;top:880px;width:360px}
  .footer{position:absolute;left:0;right:0;bottom:28px;text-align:center;font-size:14.5px;letter-spacing:.3px;color:var(--ink)}
</style>
</head>
<body>
  <main class="flyer">
    <svg class="flyer__tint" viewBox="0 0 900 1164" aria-hidden="true">
      <polygon points="0,660 420,660 470,720 470,1070 900,1070 900,590 560,820 0,820" fill="var(--paper-tint)" opacity=".7"/>
      <polygon points="0,1095 900,1040 900,1164 0,1164" fill="var(--paper-tint)" opacity=".6"/>
    </svg>

    <section class="hero" role="img" aria-label="Photo of a field technician working on high-voltage switchgear at a substation">
      <div class="hero__overlay"></div>
    </section>

    <header class="brand-tab">
      <span class="brand-tab__mark"></span>
      <span class="brand-tab__name">Falcon Breakerworks</span>
      <span class="brand-tab__tagline">A Grid Parts Group Company</span>
    </header>

    <p class="intro">Falcon Breakerworks offers an expertly trained Field Service program that can provide technical guidance and assistance for your initial installation, sustaining maintenance, and repair of equipment manufactured by Falcon Breakerworks. A 4-6 week reservation for assistance is recommended to ensure that we can fully accommodate your desired schedule. Expedited service may be available upon request.</p>

    <article class="rate-card rate-card--standard">
      <svg viewBox="0 0 360 312" preserveAspectRatio="none" aria-hidden="true">
        <polygon points="90,0 270,0 360,156 270,312 90,312 0,156" fill="var(--blue)" stroke="var(--white)" stroke-width="6"/>
        <polygon points="90,3 270,3 317,82 43,82" fill="var(--blue-light)"/>
      </svg>
      <div class="rate-card__body">
        <h2 class="rate-card__title">Standard Rates</h2>
        <p class="rate-card__sub">(on-site) up to 10 hours + travel and per diem expenses</p>
        <p class="rate-card__price">$250 x 1.00</p>
        <p class="rate-card__note">Monday through Friday rate per hour ($2500 minimum)</p>
        <p class="rate-card__price">$250 x 1.50</p>
        <p class="rate-card__note">Saturday rate per hour</p>
        <p class="rate-card__price">$250 X 2.00</p>
        <p class="rate-card__note">Sunday rate per hour</p>
      </div>
    </article>

    <article class="rate-card rate-card--premium">
      <svg viewBox="0 0 360 312" preserveAspectRatio="none" aria-hidden="true">
        <polygon points="90,0 270,0 360,156 270,312 90,312 0,156" fill="var(--orange)" stroke="var(--white)" stroke-width="6"/>
        <polygon points="90,3 270,3 317,82 43,82" fill="var(--orange-light)"/>
      </svg>
      <div class="rate-card__body">
        <h2 class="rate-card__title">Premium Rates</h2>
        <p class="rate-card__sub">(on-site) over 8 hours + travel and per diem expenses</p>
        <p class="rate-card__price">$250 x 1.50</p>
        <p class="rate-card__note">Over Time (9-12 hours) rate per hour</p>
        <p class="rate-card__price">$250 x 2.00</p>
        <p class="rate-card__note">Double Time (Over 12 hours) rate per hour</p>
        <p class="rate-card__price">$250 X 2.50</p>
        <p class="rate-card__note">Non-standard overnight hours</p>
      </div>
    </article>

    <section class="info info--minimum">
      <h3 class="info__title">Minimum Charge</h3>
      <ul>
        <li>The minimum charge, excluding travel time and expenses shall be the equivalent of one 10 hour day</li>
        <li>Cancellation charge of 4 standard hours plus any non-cancellable airfare or lodging charges shall apply</li>
        <li>Employee Drug Screening</li>
        <li>Drug screening and/or background check costs (if required by customer) shall be invoiced at actual cost plus 30%.</li>
      </ul>
    </section>

    <section class="info info--expenses">
      <h3 class="info__title">Expenses</h3>
      <ul>
        <li>Airfare - invoiced at actual cost + 25%</li>
        <li>Lodging - invoiced at actual cost + 25%</li>
        <li>Meals and Incidentals – invoiced at cost (not to exceed $100/day)</li>
        <li>Rental Vehicle and related costs – Invoiced at cost +25%</li>
      </ul>
    </section>

    <footer class="footer">1480 Cedar Ridge Rd. • Fairview, AL 35099 • 205-555-0142 • 800-555-0187 • Fax: 205-555-0163</footer>
  </main>
</body>
</html>
```